Tellmar Ridge Logistics Flyer

I need a flier that will market TELLMAR RIDGE LOGISTICS, a dispatching service for COMMERCIAL VEHICLES. I’d want the marketing material to reflect this in someway. Flier must request:

ACTIVE AUTHORITY#
COPY OF CDL
CARRIER PACKET
REFERENCES OF WORK COMPLETED
COPY OF CDL
SIGNED W-9
PROOF OF INSURANCE (Naming Our Company As The Certificate Holder)
MUST SIGN OUR LOGISTICS AGREEMENT
SECURITY DEPOSIT
(Both) Tractor & Trailer PREFERRED

```html
<!DOCTYPE html>
<html lang="en">
<head>
<meta charset="UTF-8">
<title>Tellmar Ridge Logistics Flyer</title>
<link href="https://fonts.googleapis.com/css2?family=Oswald:wght@500;600&family=Open+Sans:wght@400;600;700&display=swap" rel="stylesheet">
<style>
  :root {
    --orange: #f5ae3d;
    --ink: #2c2c2c;
    --ink-soft: #444;
    --paper: #ffffff;
    --backdrop: #ecebe8;
    --sky-top: #c9dcef;
    --sky-mid: #8fb0cf;
    --tree: #5e8a3a;
  }
  * { margin: 0; padding: 0; box-sizing: border-box; }
  html, body { width: 1200px; height: 800px; overflow: hidden; }
  body {
    background: var(--backdrop);
    font-family: "Open Sans", Arial, sans-serif;
    color: var(--ink);
    position: relative;
  }
  .flyer {
    position: absolute;
    left: 330px; top: 18px;
    width: 540px; height: 764px;
    background: var(--paper);
    overflow: hidden;
    box-shadow: 0 4px 18px rgba(0,0,0,.12);
  }
  .flyer-shapes { position: absolute; inset: 0; }
  .flyer-title {
    position: absolute;
    left: 60px; top: 62px; width: 340px;
    text-align: center;
    font-family: "Oswald", "Arial Narrow", sans-serif;
    font-weight: 500;
    font-size: 40px;
    line-height: 1.45;
    letter-spacing: 1px;
    color: var(--paper);
  }
  .section-heading {
    font-weight: 700;
    font-size: 14px;
    letter-spacing: .5px;
    margin-bottom: 8px;
  }
  .about {
    position: absolute;
    right: 32px; top: 190px; width: 200px;
    text-align: right;
  }
  .about p, .marketing p {
    font-size: 11px;
    line-height: 1.55;
    color: var(--ink-soft);
  }
  .services {
    position: absolute;
    left: 40px; top: 282px; width: 235px;
  }
  .services ul { list-style: none; }
  .services li {
    font-size: 10.5px;
    line-height: 1.5;
    color: var(--ink-soft);
    padding-left: 12px;
    position: relative;
    text-transform: uppercase;
  }
  .services li::before {
    content: "";
    position: absolute; left: 0; top: 6px;
    width: 5px; height: 5px; border-radius: 50%;
    background: var(--ink);
  }
  .services li .note { text-transform: none; }
  .marketing {
    position: absolute;
    left: 40px; top: 478px; width: 175px;
  }
  .contact {
    position: absolute;
    left: 34px; top: 640px; width: 220px;
    color: var(--paper);
  }
  .contact h3 {
    font-size: 13px; font-weight: 700;
    line-height: 1.35;
    margin-bottom: 8px;
    letter-spacing: .4px;
  }
  .contact p { font-size: 10.5px; line-height: 1.6; }
</style>
</head>
<body>
  <article class="flyer">
    <svg class="flyer-shapes" width="540" height="764" viewBox="0 0 540 764">
      <defs>
        <linearGradient id="skylineTone" x1="0" y1="0" x2="0" y2="1">
          <stop offset="0" stop-color="var(--sky-top)"/>
          <stop offset="0.65" stop-color="var(--sky-mid)"/>
          <stop offset="1" stop-color="var(--tree)"/>
        </linearGradient>
      </defs>
      <path class="header-band" d="M0 0 H540 V172 C 400 165, 220 200, 0 278 Z" fill="var(--orange)"/>
      <circle class="city-photo" cx="455" cy="545" r="180" fill="url(#skylineTone)" role="img" aria-label="City skyline of tall office towers above green trees"/>
      <path class="contact-band" d="M0 592 C 140 565, 270 590, 310 764 H0 Z" fill="var(--orange)"/>
    </svg>

    <h1 class="flyer-title">TELLMAR RIDGE<br>LOGISTICS</h1>

    <section class="about">
      <h2 class="section-heading">ABOUT US</h2>
      <p>A flyer (or flier) is a form of paper advertisement intended for wide distribution and typically posted or distributed in a public place, handed out to individuals or sent through the mail. In the 2010s, flyers range from inexpensively photocopied</p>
    </section>

    <section class="services">
      <h2 class="section-heading">OUR SERVICES</h2>
      <ul>
        <li>Active Authority# Copy of CDL</li>
        <li>Carrier Packet References of Work Completed</li>
        <li>Signed W-9 Proof of Insurance <span class="note">(Naming Our Company As The Certificate Holder)</span></li>
        <li>Must Sign Our Logistics Agreement</li>
        <li>Security Deposit</li>
        <li><span class="note">(Both)</span> Tractor &amp; Trailer Preferred</li>
      </ul>
    </section>

    <section class="marketing">
      <h2 class="section-heading">MARKETING</h2>
      <p>A flyer (or flier) is a form of paper advertisement intended for wide distribution and typically posted or distributed in a public place, handed out to</p>
    </section>

    <section class="contact">
      <h3>CONTACT US FOR<br>DETAILS:</h3>
      <p>123-456-7890</p>
      <p>www.tellmarridge.com</p>
      <p>dispatch@tellmarridge.com</p>
    </section>
  </article>
</body>
</html>
```